I need a label with logo to go on jars of honey.
Label size 70mm x 70mm
The front label should say :
The Kestrel Honey Co. (logo)
Torvale Honey
400g
The back label:
Would have nutritional information
And our address
You can see from the uploaded files the styles I prefer, I have uploaded a photo of the honey product too. The background of the logo doesn't have to be white. I would like to develop a color scheme that would look nice against the color of the honey.
The Kestrel Honey Co. / The Kestrel Honey Company

```html
<!DOCTYPE html>
<html lang="en">
<head>
<meta charset="utf-8">
<title>Torvale Honey – Front Label</title>
<link rel="stylesheet" href="https://fonts.googleapis.com/css2?family=Luckiest+Guy&family=Poppins:wght@500&display=swap">
<style>
  :root {
    --page: #f5f5f3;
    --label-mint: #bfe6e3;
    --dot-tone: #d6e9dc;
    --cocoa: #5a2a24;
    --cream: #f4eedb;
  }
  html, body {
    margin: 0;
    padding: 0;
    width: 1200px;
    height: 1200px;
    overflow: hidden;
    background: var(--page);
  }
  .canvas {
    position: relative;
    width: 1200px;
    height: 1200px;
  }
  .front-label {
    position: absolute;
    left: 100px;
    top: 120px;
    width: 1000px;
    height: 960px;
    display: block;
  }
  .label-ground { fill: var(--label-mint); }
  .brand-ring {
    fill: none;
    stroke: var(--cocoa);
    stroke-width: 5;
  }
  .brand-name {
    font-family: "Poppins", "Helvetica Neue", Arial, sans-serif;
    font-weight: 500;
    font-size: 28px;
    letter-spacing: 5px;
    fill: var(--cocoa);
  }
  .title-blob { fill: var(--cocoa); }
  .product-title {
    font-family: "Luckiest Guy", Impact, "Arial Black", sans-serif;
    font-size: 128px;
    fill: var(--cream);
  }
  .net-weight {
    font-family: "Luckiest Guy", Impact, "Arial Black", sans-serif;
    font-size: 32px;
    letter-spacing: 1px;
    fill: var(--cocoa);
  }
</style>
</head>
<body>
<div class="canvas">
  <svg class="front-label" viewBox="0 0 1000 960" xmlns="http://www.w3.org/2000/svg" aria-labelledby="label-title">
    <title id="label-title">Torvale Honey front label, 400g, by The Kestrel Honey Co.</title>
    <defs>
      <linearGradient id="dot-field-tone" x1="0" y1="0" x2="0" y2="1">
        <stop offset="0" stop-color="#bfe6e3"/>
        <stop offset="0.3" stop-color="#cfe7dc"/>
        <stop offset="1" stop-color="#d9e9dc"/>
      </linearGradient>
    </defs>

    <rect class="label-ground" x="0" y="0" width="1000" height="960"/>

    <g role="img" aria-label="Cream halftone dot pattern fading in across the lower half of the label">
      <rect x="0" y="380" width="1000" height="580" fill="url(#dot-field-tone)"/>
    </g>

    <g class="brand-mark">
      <circle class="brand-ring" cx="470" cy="210" r="125"/>
      <text class="brand-name" x="500" y="400" text-anchor="middle">THE KESTREL HONEY CO.</text>
    </g>

    <path class="title-blob"
      d="M200,478 Q188,436 236,434 L384,434 Q414,434 424,452 L752,452
         Q832,456 832,566 L826,742 Q820,834 736,838 L304,852
         Q192,856 186,742 L180,586 Q178,506 200,478 Z"/>

    <text class="product-title" x="506" y="665" text-anchor="middle"
          textLength="560" lengthAdjust="spacingAndGlyphs">TORVALE</text>
    <text class="product-title" x="506" y="805" text-anchor="middle"
          textLength="470" lengthAdjust="spacingAndGlyphs">HONEY</text>

    <text class="net-weight" x="740" y="892" text-anchor="middle">400G</text>
  </svg>
</div>
</body>
</html>
```